Small but growing painting company. Have built up a steady client base. Want to start having a more professional look. Want to start with changing my business cards, and also getting new logo and tee shirts.

Target Market(s)

Home owners, property management companies, all ages 30-70

Industry/Entity Type

Painting And Decorating

Contact Information for Business Card

Bright Ridge Painting LLC Mark Delvecchi 630-584-3907 interior, exterior, vaulted ceiling, drywall repair, pressure washing, kitchen cabinets, epoxy, garage floors,

Font styles to use
Sans Serif
Other font styles liked:
• Harrington

Colors
0355a3
ffffff
ec1f27
000000
3176b5
0493ce
474747
b7b7b7

Requirements
Must have
• Creative, something that doesn’t look like every other painting card.
Nice to have
• I would like something with an arrow or something going to a point

```html
<!DOCTYPE html>
<html lang="en">
<head>
<meta charset="utf-8">
<title>Bright Ridge Painting LLC – Business Card</title>
<link href="https://fonts.googleapis.com/css2?family=Arimo:wght@400;700&display=swap" rel="stylesheet">
<style>
  :root {
    --backdrop: #e5ddd6;
    --card-white: #f2f3f5;
    --brand-blue: #2e75b6;
    --ink: #111111;
    --band-light: #b9b9ba;
    --band-dark: #767779;
    --white: #ffffff;
  }
  * { margin: 0; padding: 0; box-sizing: border-box; }
  html, body {
    width: 1200px;
    height: 1200px;
    overflow: hidden;
    background: var(--backdrop);
    font-family: "Arimo", Arial, sans-serif;
  }
  .card {
    position: absolute;
    left: 272px;
    top: 394px;
    width: 693px;
    height: 396px;
    background: var(--card-white);
    overflow: hidden;
  }
  .brand {
    position: absolute;
    left: 0;
    right: 0;
    top: 76px;
    display: flex;
    align-items: center;
    justify-content: center;
    gap: 16px;
    color: var(--brand-blue);
    font-weight: 700;
    font-size: 42px;
    letter-spacing: 0.5px;
  }
  .brand-square {
    width: 30px;
    height: 30px;
    background: var(--brand-blue);
  }
  .services {
    position: absolute;
    left: 0;
    right: 0;
    top: 176px;
    text-align: center;
    color: var(--ink);
    font-size: 17px;
    line-height: 28px;
    letter-spacing: 1px;
  }
  .contact-band {
    position: absolute;
    left: 0;
    top: 256px;
    width: 693px;
    height: 140px;
  }
  .contact-name,
  .contact-phone {
    position: absolute;
    top: 322px;
    color: var(--white);
    font-size: 40px;
    line-height: 44px;
  }
  .contact-name { left: 28px; }
  .contact-name strong { font-weight: 700; }
  .contact-phone {
    right: 28px;
    font-weight: 700;
    font-size: 37px;
  }
</style>
</head>
<body>
  <div class="card">
    <div class="brand">
      <span class="brand-square"></span>
      <span class="brand-name">Bright Ridge Painting LLC</span>
    </div>

    <p class="services">
      Interior, Exterior, Vaulted Ceiling,<br>
      Drywall Repair, Pressure Washing,<br>
      Kitchen Cabinets, Epoxy, Garage Floors
    </p>

    <svg class="contact-band" viewBox="0 0 693 140" preserveAspectRatio="none" aria-hidden="true">
      <defs>
        <linearGradient id="bandShade" x1="0" y1="0" x2="0" y2="1">
          <stop offset="0" stop-color="var(--band-light)"/>
          <stop offset="0.55" stop-color="#a9aaab"/>
          <stop offset="1" stop-color="var(--band-dark)"/>
        </linearGradient>
      </defs>
      <path d="M0 8 L40 6 L70 2 L110 5 L200 8 L300 6 L400 9 L500 7 L600 4 L693 8 L693 140 L0 140 Z" fill="url(#bandShade)"/>
    </svg>

    <div class="contact-name">Mark<strong>Delvecchi</strong></div>
    <div class="contact-phone">630-584-3907</div>
  </div>
</body>
</html>
```